business card deign

Logo needs the following on it.
1. attached logo
2. Tagline - "If it keeps a drink cold or the party going...we do it!"
3. Name- Dalia Fenwick, Founder and CPO
4. Address - 482 E. Calder Avenue, Ste 2207, Tampa, FL. 33719
5. Phone - 720.555.0183

```html
<!DOCTYPE html>
<html lang="en">
<head>
<meta charset="utf-8">
<title>Hopwell Business Card</title>
<link rel="stylesheet" href="https://fonts.googleapis.com/css2?family=Montserrat:wght@400;500;800&display=swap">
<style>
  :root {
    --backdrop: #ece9e4;
    --card: #ffffff;
    --ink: #111111;
    --rule: #222222;
  }
  * { box-sizing: border-box; margin: 0; padding: 0; }
  html, body {
    width: 1200px;
    height: 931px;
    overflow: hidden;
    background: var(--backdrop);
    font-family: "Montserrat", sans-serif;
    color: var(--ink);
  }
  .sheet {
    width: 1200px;
    height: 931px;
    display: flex;
    flex-direction: column;
    align-items: center;
    justify-content: center;
    gap: 40px;
  }
  .card {
    width: 700px;
    height: 400px;
    background: var(--card);
    border-radius: 22px;
    box-shadow: 0 6px 18px rgba(0,0,0,0.12);
    position: relative;
  }
  .card--front {
    display: flex;
    align-items: center;
    justify-content: center;
  }
  .wordmark {
    display: flex;
    align-items: center;
    gap: 18px;
  }
  .wordmark__dot {
    width: 22px;
    height: 22px;
    border-radius: 50%;
    background: var(--ink);
  }
  .wordmark__name {
    font-weight: 800;
    font-size: 50px;
    letter-spacing: 0.32em;
    text-transform: uppercase;
  }
  .card--back .wordmark {
    position: absolute;
    left: 60px;
    top: 176px;
    gap: 12px;
  }
  .card--back .wordmark__dot { width: 14px; height: 14px; }
  .card--back .wordmark__name { font-size: 30px; }
  .divider {
    position: absolute;
    left: 342px;
    top: 96px;
    width: 1.5px;
    height: 150px;
    background: var(--rule);
  }
  .contact {
    position: absolute;
    left: 372px;
    top: 92px;
  }
  .contact__name {
    font-weight: 800;
    font-size: 22px;
    text-transform: uppercase;
    letter-spacing: 0.02em;
  }
  .contact__title {
    font-size: 18px;
    margin-top: 2px;
    letter-spacing: 0.03em;
  }
  .contact__list {
    list-style: none;
    margin-top: 24px;
    font-size: 17px;
    line-height: 1.3;
  }
  .contact__item {
    display: flex;
    align-items: flex-start;
    gap: 10px;
  }
  .contact__icon { width: 16px; height: 18px; flex: none; margin-top: 2px; }
  .tagline {
    position: absolute;
    left: 0;
    right: 0;
    bottom: 58px;
    text-align: center;
    font-size: 19px;
    font-weight: 500;
  }
</style>
</head>
<body>
<main class="sheet">
  <section class="card card--front" aria-label="Card front">
    <div class="wordmark">
      <span class="wordmark__dot"></span>
      <span class="wordmark__name">Hopwell</span>
    </div>
  </section>

  <section class="card card--back" aria-label="Card back">
    <div class="wordmark">
      <span class="wordmark__dot"></span>
      <span class="wordmark__name">Hopwell</span>
    </div>
    <div class="divider"></div>
    <div class="contact">
      <p class="contact__name">Dalia Fenwick</p>
      <p class="contact__title">Founder and CPO</p>
      <ul class="contact__list">
        <li class="contact__item">
          <svg class="contact__icon" viewBox="0 0 16 16" aria-hidden="true">
            <path fill="#111" d="M3.6 1.2l2.3 2.9-1.4 1.7c.9 2 2.6 3.8 4.7 4.7l1.7-1.4 2.9 2.3-1.2 2.6C7.5 14 2 8.5 1 2.4z"/>
          </svg>
          <span>720.555.0183</span>
        </li>
        <li class="contact__item">
          <svg class="contact__icon" viewBox="0 0 16 20" aria-hidden="true">
            <path fill="#111" d="M8 0a7 7 0 0 0-7 7c0 5 7 13 7 13s7-8 7-13a7 7 0 0 0-7-7zm0 10a3 3 0 1 1 0-6 3 3 0 0 1 0 6z"/>
          </svg>
          <span>482 E. Calder Avenue, Ste<br>2207, Tampa, FL. 33719</span>
        </li>
      </ul>
    </div>
    <p class="tagline">If it keeps a drink cold or the party going...we do it!</p>
  </section>
</main>
</body>
</html>
```